sticker of engine oil bottle

Dear Designers
i want to design new sticker for my bottle engine oil brand
i want the sticker creative and get harmonic with the bottle color one Blue and another color Red
my brand name is (Vesko) as attached logo and pictures and i will attached pictures you can take ideas from it
The Shape of Plastic bottle i used is the first bottle attached in blue color Vesko 20W50 and in red color vesko 5W30
i want new creative design calms colors and designs
and not copy paste from another design

Target Market(s)

car care and engine oil service centers

Requirements
Must have
• companies approvals and certificates
Nice to have
• new idea
Should not have
• copy past from another design on internet

```html
<!DOCTYPE html>
<html lang="en">
<head>
<meta charset="utf-8">
<title>Vesko HD SAE 50 Label</title>
<link rel="stylesheet" href="https://fonts.googleapis.com/css2?family=Orbitron:wght@700;800;900&family=Graduate&display=swap">
<style>
  :root {
    --backdrop: #c8b098;
    --navy-deep: #2f3358;
    --navy: #33437e;
    --silver-light: #f4f4f4;
    --silver-mid: #b9b9b9;
    --silver-dark: #6e6e6e;
    --band-black: #0d0d0d;
    --white: #ffffff;
    --badge-gold: #a57a45;
    --badge-paper: #e7ddd6;
  }
  * { margin: 0; padding: 0; box-sizing: border-box; }
  html, body { width: 1082px; height: 1200px; overflow: hidden; }
  body { background: var(--backdrop); position: relative; font-family: "Orbitron", sans-serif; }
  .label {
    position: absolute; left: 288px; top: 179px; width: 556px; height: 824px;
    box-shadow: 10px 12px 14px rgba(0,0,0,0.45);
    border-top: 4px solid #9a9a9a; border-left: 4px solid #9a9a9a;
    overflow: hidden;
  }
  .label svg { display: block; width: 100%; height: 100%; }
  .brand-name { font-family: "Orbitron", sans-serif; font-weight: 800; fill: var(--white); }
  .grade-hd { font-family: "Orbitron", sans-serif; font-weight: 900; font-style: italic; fill: url(#hd-grey); }
  .grade-sae { font-family: "Orbitron", sans-serif; font-weight: 800; fill: var(--white); }
  .grade-api { font-family: "Orbitron", sans-serif; font-weight: 700; fill: var(--white); }
  .grade-num { font-family: "Orbitron", sans-serif; font-weight: 900; fill: var(--white); }
  .tagline { font-family: "Orbitron", sans-serif; font-weight: 800; font-style: italic; fill: var(--white); }
  .volume { font-family: "Graduate", serif; fill: var(--white); stroke: var(--navy-deep); stroke-width: 2; }
  .seal-name { font-family: "Orbitron", sans-serif; font-weight: 800; fill: var(--navy); }
</style>
</head>
<body>
  <div class="label">
    <svg viewBox="0 0 556 824" xmlns="http://www.w3.org/2000/svg">
      <defs>
        <linearGradient id="silver" x1="0" y1="0" x2="1" y2="0.3">
          <stop offset="0" stop-color="var(--silver-dark)"/>
          <stop offset="0.25" stop-color="var(--silver-light)"/>
          <stop offset="0.5" stop-color="var(--silver-mid)"/>
          <stop offset="0.75" stop-color="var(--silver-light)"/>
          <stop offset="1" stop-color="var(--silver-dark)"/>
        </linearGradient>
        <linearGradient id="navy-top" x1="0" y1="0" x2="1" y2="1">
          <stop offset="0" stop-color="var(--navy-deep)"/>
          <stop offset="0.5" stop-color="var(--navy)"/>
          <stop offset="1" stop-color="var(--navy-deep)"/>
        </linearGradient>
        <linearGradient id="navy-side" x1="0" y1="0" x2="0" y2="1">
          <stop offset="0" stop-color="var(--navy-deep)"/>
          <stop offset="0.5" stop-color="var(--navy)"/>
          <stop offset="1" stop-color="var(--navy-deep)"/>
        </linearGradient>
        <linearGradient id="band" x1="0" y1="0" x2="1" y2="0">
          <stop offset="0" stop-color="#1c1c1c"/>
          <stop offset="0.5" stop-color="#3a3a3a"/>
          <stop offset="1" stop-color="var(--band-black)"/>
        </linearGradient>
        <linearGradient id="hd-grey" x1="0" y1="0" x2="1" y2="1">
          <stop offset="0" stop-color="#6b6b6b"/>
          <stop offset="0.5" stop-color="#e6e6e6"/>
          <stop offset="1" stop-color="#8a8a8a"/>
        </linearGradient>
      </defs>

      <!-- base metal -->
      <rect class="metal-base" width="556" height="824" fill="url(#silver)"/>

      <!-- upper right navy field with swoosh -->
      <path class="field-top" d="M78 0 L556 0 L556 276 C410 262 250 190 160 80 Q130 40 112 0 Z" fill="url(#navy-top)"/>
      <path class="swoosh-edge" d="M112 0 Q130 40 160 80 C250 190 410 262 556 276" fill="none" stroke="var(--white)" stroke-width="2"/>
      <path class="swoosh-lower" d="M70 0 Q95 90 170 170 C270 290 420 360 556 385" fill="none" stroke="var(--white)" stroke-width="2"/>

      <!-- lower left navy field -->
      <polygon class="field-side" points="0,199 249,824 0,824" fill="url(#navy-side)"/>
      <line x1="0" y1="199" x2="249" y2="824" stroke="var(--white)" stroke-width="2"/>
      <line x1="0" y1="100" x2="420" y2="824" stroke="var(--white)" stroke-width="1.5"/>

      <!-- dark diagonal band -->
      <polygon class="band" points="0,5 556,661 556,824 418,824 0,50" fill="url(#band)"/>
      <line x1="0" y1="5" x2="556" y2="661" stroke="var(--white)" stroke-width="2"/>
      <line x1="0" y1="50" x2="418" y2="824" stroke="var(--white)" stroke-width="2"/>
      <g class="band-stripes" stroke="#8d8d8d" stroke-width="2">
        <line x1="120" y1="170" x2="556" y2="700"/>
        <line x1="110" y1="195" x2="556" y2="745"/>
        <line x1="100" y1="220" x2="540" y2="800"/>
        <line x1="90" y1="245" x2="500" y2="824"/>
      </g>

      <text class="tagline" x="0" y="0" font-size="23" textLength="850" lengthAdjust="spacingAndGlyphs"
            transform="translate(40 92) rotate(56.1)">HIGH POWER TECHNOLOGY MOTOR ENGINE OIL ACTIVE</text>

      <!-- brand block -->
      <circle class="brand-mark" cx="208" cy="75" r="44" fill="var(--white)"/>
      <text class="brand-name" x="272" y="82" font-size="39" textLength="252" lengthAdjust="spacingAndGlyphs">VESKO</text>
      <line x1="270" y1="89" x2="526" y2="89" stroke="var(--white)" stroke-width="2.5"/>

      <!-- grade block -->
      <text class="grade-hd" x="262" y="144" font-size="46">HD</text>
      <text class="grade-sae" x="261" y="179" font-size="31" textLength="106" lengthAdjust="spacingAndGlyphs">SAE</text>
      <text class="grade-api" x="409" y="117" font-size="14" textLength="98" lengthAdjust="spacingAndGlyphs">API CF-4</text>
      <text class="grade-num" x="404" y="178" font-size="66" textLength="110" lengthAdjust="spacingAndGlyphs">50</text>

      <!-- side column -->
      <circle class="seal" cx="58" cy="473" r="31" fill="var(--white)"/>
      <text class="seal-name" x="58" y="477" font-size="11" text-anchor="middle">VESKO</text>

      <text class="volume" x="18" y="626" font-size="120" textLength="112" lengthAdjust="spacingAndGlyphs">6L</text>

      <rect class="truck-art" x="37" y="632" width="84" height="65" rx="6" fill="#3c3c46"
            role="img" aria-label="Illustration of a heavy goods truck"/>

      <g class="approval-badges">
        <rect x="28" y="705" width="52" height="35" fill="var(--badge-paper)"/>
        <rect x="82" y="705" width="26" height="35" fill="#3a2b28"/>
        <rect x="110" y="705" width="19" height="35" fill="var(--badge-paper)"/>
      </g>
      <circle class="cert-badge" cx="49" cy="781" r="27" fill="var(--badge-gold)"/>
      <circle class="cert-badge" cx="108" cy="781" r="27" fill="#cfcfcf"/>
    </svg>
  </div>
</body>
</html>
```